依頼詳細
下記ブランドコンセプトに沿ったご提案をお願い致します。
プロトタイプを添付いたします。構成等、より優れていると思えるご提案がありましたら無視して頂いて構いません。
ブランドコンセプトは以下の通りです。

-- 以下、ブランドコンセプト
「自然が持つ美しさ」と「暮らす人の思い」を取り入れ『生活が楽しい住まい』を創ります
人々に永く愛されてきた天然素材を使用することで自然素材だけが持つ色や質感から確かな手触りと温もりを暮らす人に与え続けてくれます。新しいだけを追い過ぎず自然素材の持つ機能性を生かして自然の働きでしっかりと家を守る
それは流行に左右されない気品を保つ「素朴で美しい風合い」に仕上がります。

住む人のライフスタイルや好みをしっかりとお聞かせいただいた上で土地を生かし隣地環境と調和のある設計を企画し、その人らしい家を一緒に考えていきます。
それはその人がどんなふうに暮らしていきたいのかを一緒に考え、その地で永く暮らしていくイメージを膨らませ生活が楽しくなる様な空間を提案します。
-- 以上、ブランドコンセプト
サイトURL
http://morvatu.com/
ページ数
1ページ
希望イメージ
シンプル 複雑
単色 カラフル
暗い 明るい
日常 高級
遊び心 厳粛
未来的 伝統的
女性的 男性的
希望する色
納品ファイル
補足説明
トップページに関するプロトタイプを「トップページ.png」として添付しております。
また、素材として利用可能なものは下記dropboxリンクよりご利用ください。
https://www.filqeno-share.com/sh/7kdpqe31vmx02z/QWkrtyuu_pLmNnbvZxCdeRtYsUoPw?dl=0

■ 選んだ理由

全員が色使いやコンテンツの配置などを理由として同デザインを選択しました。
似通ったデザインの中でも全員の目を引く、魅力的な部分があったのだと考えます。

■ 提案者全員のお礼・コメント

今回は多くの皆様に貴重なお時間を使って頂きご提案頂きました事、大変うれしく思い感謝申し上げます。
複数名で選考を行いましたが、選考するメンバー全員でどれも素晴らしいデザインだよねと口をそろえて申しておりました。

本当にありがとうございました。

```html
<!DOCTYPE html>
<html lang="ja">
<head>
<meta charset="utf-8">
<title>Morvatu | 自然素材の注文住宅</title>
<link href="https://fonts.googleapis.com/css2?family=Noto+Sans+JP:wght@400;500;700&family=Lora:ital,wght@0,500;1,500&display=swap" rel="stylesheet">
<style>
:root{
  --cream:#f3eedd;
  --cream-deep:#efe7cf;
  --band:#f6f0d4;
  --olive:#a8923a;
  --gold:#e6c446;
  --brown:#5a4a3a;
  --dark:#4b4036;
  --darker:#3c332b;
  --text:#4a4440;
  --muted:#8a8276;
  --line:#ddd5bf;
  --white:#ffffff;
  --photo-wood:#c9ad86;
  --photo-sky:#b9c6cf;
  --photo-room:#d8cab2;
}
*{margin:0;padding:0;box-sizing:border-box}
html,body{width:1200px;height:2376px;overflow:hidden}
body{font-family:"Noto Sans JP",sans-serif;color:var(--text);background:var(--white);font-size:12px;line-height:1.7}
.wrap{width:880px;margin:0 auto;position:relative}
a{color:inherit;text-decoration:none}

/* header */
.site-header{height:118px;position:relative}
.site-header .tagline{position:absolute;left:0;top:6px;font-size:10px;color:var(--muted)}
.brand{position:absolute;left:0;top:36px;display:flex;align-items:center;gap:10px}
.brand .mark{width:30px;height:30px;background:var(--olive)}
.brand .name{font-size:30px;font-weight:700;color:var(--brown);letter-spacing:.04em}
.header-links{position:absolute;right:0;top:12px;display:flex;gap:8px}
.header-links span{font-size:10px;background:var(--cream);padding:2px 10px;border:1px solid var(--line)}
.phone{position:absolute;right:0;top:40px;display:flex;align-items:center;gap:8px;color:var(--brown)}
.phone .num{font-size:30px;font-weight:700;letter-spacing:.02em}
.phone-note{position:absolute;right:0;top:80px;font-size:10px;color:var(--muted)}

.global-nav{height:40px;background:var(--cream)}
.global-nav ul{list-style:none;display:flex;width:880px;margin:0 auto;height:40px}
.global-nav li{flex:1;text-align:center;line-height:40px;font-size:13px;font-weight:500;color:var(--brown);border-left:1px solid var(--line)}
.global-nav li:last-child{border-right:1px solid var(--line)}
.global-nav li.current{background:var(--gold);color:var(--white)}

/* hero */
.hero{height:360px;background:var(--cream-deep);position:relative;overflow:hidden}
.hero .side{position:absolute;top:12px;width:200px;height:320px;background:linear-gradient(160deg,#e2d6bf,#cdbb9c);opacity:.5}
.hero .side.left{left:-40px}.hero .side.right{right:-40px}
.hero .slide{position:absolute;left:160px;top:12px;width:880px;height:320px;background:linear-gradient(170deg,var(--photo-sky) 0%,#e3dccc 40%,var(--photo-wood) 75%,#9f8a6b 100%)}
.hero .caption{position:absolute;left:30px;bottom:26px}
.hero .caption p{display:inline-block;background:rgba(255,255,255,.88);color:var(--olive);font-weight:700;padding:2px 10px;margin-top:6px}
.hero .caption .small{font-size:14px}
.hero .caption .big{font-size:22px}
.hero .arrow{position:absolute;top:150px;width:34px;height:34px;border-radius:50%;background:rgba(255,255,255,.85)}
.hero .arrow.prev{left:176px}.hero .arrow.next{right:176px}
.hero .dots{position:absolute;bottom:8px;left:0;right:0;display:flex;justify-content:center;gap:8px}
.hero .dots i{width:8px;height:8px;border-radius:50%;background:#cfc4a8}
.hero .dots i.on{background:var(--olive)}

/* section head */
.sec-head{display:flex;align-items:flex-end;gap:10px;border-bottom:1px solid var(--line);padding-bottom:6px;margin-bottom:18px}
.sec-head h2{font-family:"Lora",serif;font-weight:500;font-size:26px;color:var(--brown);line-height:1}
.sec-head small{font-size:10px;color:var(--muted)}
.sec-head .more{margin-left:auto;font-size:10px;color:var(--muted)}

/* concept */
.concept{padding-top:34px;height:360px}
.concept .body{display:flex;gap:24px}
.concept .text{width:460px}
.concept .lead{font-size:16px;font-weight:700;color:var(--olive);line-height:1.8;margin-bottom:14px}
.concept .text p{font-size:11px;margin-bottom:10px}
.concept .photos{width:396px;display:grid;grid-template-columns:1fr 1fr;gap:8px}
.concept .photos .main{grid-column:1/3;height:140px;background:linear-gradient(150deg,var(--photo-room),#b79d78)}
.concept .photos .sub{height:118px;background:linear-gradient(150deg,#e4d9c4,var(--photo-wood))}

/* contents */
.contents{height:330px;padding-top:10px}
.cards{display:flex;justify-content:space-between}
.card{width:280px}
.card .img{height:190px;background:linear-gradient(160deg,#dccfb6,#a88d68)}
.card .label{display:flex;align-items:center;gap:8px;padding:10px 4px;border-bottom:1px solid var(--line);font-weight:700;color:var(--brown);font-size:13px}
.card .label .dot{width:16px;height:16px;border-radius:50%;background:var(--gold)}

/* works */
.works{background:var(--band);height:330px;padding-top:30px}
.works-row{display:flex;justify-content:space-between;position:relative}
.work{width:205px;text-align:center;font-size:10px;color:var(--muted)}
.work .img{height:140px;background:linear-gradient(175deg,#c7d3da 0%,#eee8da 45%,#b8a98e 100%);margin-bottom:6px}
.works .arrow{position:absolute;top:56px;width:26px;height:26px;border-radius:50%;background:var(--white)}
.works .arrow.prev{left:-40px}.works .arrow.next{right:-40px}

/* news */
.news-area{height:400px;padding-top:30px;display:flex;gap:30px}
.news{width:550px}
.news-item{display:flex;gap:14px;padding:10px 0;border-bottom:1px dotted var(--line)}
.news-item .thumb{width:92px;height:60px;background:#e6e3dd;flex:none}
.news-item h3{font-size:12px;font-weight:700;color:var(--brown)}
.news-item p{font-size:10px;color:var(--muted);line-height:1.6}
.social{width:300px;border:1px solid var(--line)}
.social .head{background:var(--cream);padding:6px 10px;font-size:11px;font-weight:700;color:var(--brown)}
.social .post{padding:10px;border-bottom:1px solid var(--line);font-size:10px;color:var(--muted)}
.social .post b{display:block;color:var(--brown);font-size:11px}
.social .post .pic{height:50px;background:#ebe6da;margin-top:6px}

/* footer */
.site-footer{background:var(--dark);height:408px;color:#e8e1d3;position:relative}
.cta{width:700px;margin:0 auto;position:relative;top:36px;display:flex;background:var(--white);height:96px}
.cta .ask{width:130px;background:var(--gold);color:var(--white);font-weight:700;font-size:14px;display:flex;flex-direction:column;align-items:center;justify-content:center;line-height:1.4}
.cta .ask small{font-size:9px;font-weight:400}
.cta .tel{flex:1;padding:14px 20px;color:var(--brown)}
.cta .tel p{font-size:10px;color:var(--muted)}
.cta .tel .num{font-size:28px;font-weight:700;display:flex;align-items:center;gap:8px;line-height:1.3}
.cta .btns{width:150px;padding:16px 14px;display:flex;flex-direction:column;gap:8px}
.cta .btns span{border:1px solid var(--olive);color:var(--olive);font-size:11px;text-align:center;padding:4px 0}
.foot-links{width:880px;margin:80px auto 0;display:flex;gap:40px;font-size:10px}
.foot-links ul{list-style:none}
.foot-links li{padding:3px 0 3px 10px;border-left:2px solid var(--olive);margin-bottom:6px}
.foot-brand{margin-left:auto;text-align:right}
.foot-brand .name{display:flex;align-items:center;gap:8px;justify-content:flex-end;font-size:22px;font-weight:700;color:var(--white)}
.foot-brand .name i{width:22px;height:22px;background:var(--gold)}
.foot-brand p{font-size:10px;margin-top:6px}
.copyright{position:absolute;bottom:0;left:0;right:0;height:26px;line-height:26px;text-align:center;font-size:9px;background:var(--darker)}
</style>
</head>
<body>

<header class="site-header wrap">
  <p class="tagline">長野県の注文住宅なら自然素材にこだわる Morvatu の家づくり</p>
  <div class="brand"><span class="mark"></span><span class="name">Morvatu</span></div>
  <div class="header-links"><span>資料請求</span><span>お問い合わせ</span></div>
  <div class="phone">
    <svg width="26" height="26" viewBox="0 0 24 24"><path fill="#a8923a" d="M6.6 10.8a15 15 0 0 0 6.6 6.6l2.2-2.2c.3-.3.7-.4 1-.2 1.1.4 2.3.6 3.6.6.6 0 1 .4 1 1V20c0 .6-.4 1-1 1A17 17 0 0 1 3 4c0-.6.4-1 1-1h3.5c.6 0 1 .4 1 1 0 1.3.2 2.5.6 3.6.1.3 0 .7-.2 1z"/></svg>
    <span class="num">0265-40-7712</span>
  </div>
  <p class="phone-note">受付時間 9:00〜18:00（水曜定休）</p>
</header>

<nav class="global-nav">
  <ul>
    <li class="current">HOME</li><li>家づくり</li><li>施工事例</li><li>お客様の声</li><li>スタッフ紹介</li><li>会社概要</li>
  </ul>
</nav>

<section class="hero">
  <div class="side left"></div><div class="side right"></div>
  <div class="slide" role="img" aria-label="木のぬくもりある外観の住宅と空">
    <div class="caption">
      <p class="small">「自然の持つ美しさ」と「暮らす人の思い」を取り入れ</p><br>
      <p class="big">『生活が楽しい住まい』を創ります。</p>
    </div>
  </div>
  <span class="arrow prev"></span><span class="arrow next"></span>
  <div class="dots"><i class="on"></i><i></i><i></i><i></i></div>
</section>

<section class="concept wrap">
  <div class="sec-head"><svg width="22" height="22" viewBox="0 0 24 24"><path fill="#a8923a" d="M4 20C4 10 10 4 20 4c0 10-6 16-16 16z"/></svg><h2>Concept</h2><small>Morvatuのこだわり</small></div>
  <div class="body">
    <div class="text">
      <p class="lead">「自然が持つ美しさ」と「暮らす人の思い」を取り入れ<br>『生活が楽しい住まい』を創ります。</p>
      <p>人々に永く愛されてきた天然素材を使用することで、自然素材だけが持つ色や質感から確かな手触りと温もりを暮らす人に与え続けてくれます。</p>
      <p>新しいだけを追い過ぎず自然素材の持つ機能性を生かして、自然の働きでしっかりと家を守る。それは流行に左右されない気品を保つ「素朴で美しい風合い」に仕上がります。</p>
      <p>住む人のライフスタイルや好みをしっかりとお聞かせいただいた上で、土地を生かし隣地環境と調和のある設計を企画し、その人らしい家を一緒に考えていきます。</p>
    </div>
    <div class="photos">
      <div class="main" role="img" aria-label="自然素材を使ったリビング"></div>
      <div class="sub" role="img" aria-label="無垢材の床と階段"></div>
      <div class="sub" role="img" aria-label="木製の棚がある室内"></div>
    </div>
  </div>
</section>

<section class="contents wrap">
  <div class="sec-head"><svg width="22" height="22" viewBox="0 0 24 24"><path fill="#a8923a" d="M4 20C4 10 10 4 20 4c0 10-6 16-16 16z"/></svg><h2>Contents</h2><small>コンテンツ</small></div>
  <div class="cards">
    <div class="card"><div class="img" role="img" aria-label="家づくりの作業風景"></div><div class="label"><span class="dot"></span>Morvatuの家づくり</div></div>
    <div class="card"><div class="img" role="img" aria-label="お客様の住まいの室内"></div><div class="label"><span class="dot"></span>お客様の声</div></div>
    <div class="card"><div class="img" role="img" aria-label="スタッフの集合写真"></div><div class="label"><span class="dot"></span>スタッフ紹介</div></div>
  </div>
</section>

<section class="works">
  <div class="wrap">
    <div class="sec-head"><svg width="22" height="22" viewBox="0 0 24 24"><path fill="#a8923a" d="M4 20C4 10 10 4 20 4c0 10-6 16-16 16z"/></svg><h2>Works</h2><small>施工事例</small><span class="more">一覧を見る ›</span></div>
    <div class="works-row">
      <span class="arrow prev"></span>
      <div class="work"><div class="img" role="img" aria-label="施工事例の住宅外観"></div>伊那市 自然素材の平屋</div>
      <div class="work"><div class="img" role="img" aria-label="施工事例の住宅外観"></div>駒ヶ根市 木の香る二階建て</div>
      <div class="work"><div class="img" role="img" aria-label="施工事例の住宅外観"></div>箕輪町 家族の集う住まい</div>
      <div class="work"><div class="img" role="img" aria-label="施工事例の住宅外観"></div>南箕輪村 庭とつながる家</div>
      <span class="arrow next"></span>
    </div>
  </div>
</section>

<section class="news-area wrap">
  <div class="news">
    <div class="sec-head"><svg width="22" height="22" viewBox="0 0 24 24"><path fill="#a8923a" d="M4 20C4 10 10 4 20 4c0 10-6 16-16 16z"/></svg><h2>News</h2><small>最新情報</small><span class="more">一覧を見る ›</span></div>
    <div class="news-item"><div class="thumb"></div><div><h3>完成見学会のお知らせ</h3><p>自然素材の住まいを実際にご覧いただける見学会を今月末に開催します。ぜひお気軽にご来場ください。</p></div></div>
    <div class="news-item"><div class="thumb"></div><div><h3>施工事例を更新しました</h3><p>木のぬくもりを感じる二階建ての住まいを施工事例に追加しました。詳しくは事例ページをご覧ください。</p></div></div>
    <div class="news-item"><div class="thumb"></div><div><h3>家づくり相談会を開催</h3><p>土地探しから資金計画まで、家づくりの疑問に丁寧にお答えする個別相談会を毎週末に行っています。</p></div></div>
    <div class="news-item"><div class="thumb"></div><div><h3>年末年始の休業について</h3><p>誠に勝手ながら年末年始は休業とさせていただきます。期間中のお問い合わせは順次対応いたします。</p></div></div>
  </div>
  <aside class="social">
    <div class="head">Socialnoteもチェック</div>
    <div class="post"><b>Morvatu</b>現場の様子や季節の暮らしの話題をお届けしています。</div>
    <div class="post"><b>Morvatu</b>新しい施工事例の写真を公開しました。木の表情をご覧ください。<div class="pic"></div></div>
    <div class="post"><b>Morvatu</b>今週末は完成見学会です。皆様のご来場をお待ちしています。</div>
  </aside>
</section>

<footer class="site-footer">
  <div class="cta">
    <div class="ask">お問い合わせ<small>お気軽にどうぞ</small></div>
    <div class="tel">
      <p>家づくりのご相談・資料請求はお電話またはフォームから</p>
      <div class="num"><svg width="22" height="22" viewBox="0 0 24 24"><path fill="#a8923a" d="M6.6 10.8a15 15 0 0 0 6.6 6.6l2.2-2.2c.3-.3.7-.4 1-.2 1.1.4 2.3.6 3.6.6.6 0 1 .4 1 1V20c0 .6-.4 1-1 1A17 17 0 0 1 3 4c0-.6.4-1 1-1h3.5c.6 0 1 .4 1 1 0 1.3.2 2.5.6 3.6.1.3 0 .7-.2 1z"/></svg>0265-40-7712</div>
      <p>受付時間 9:00〜18:00（水曜定休）</p>
    </div>
    <div class="btns"><span>資料請求</span><span>メールでのお問い合わせ</span></div>
  </div>
  <div class="foot-links">
    <ul><li>HOME</li><li>家づくり</li><li>施工事例</li></ul>
    <ul><li>お客様の声</li><li>スタッフ紹介</li><li>会社概要</li></ul>
    <ul><li>最新情報</li><li>お問い合わせ</li><li>サイトマップ</li></ul>
    <div class="foot-brand">
      <div class="name"><i></i>Morvatu</div>
      <p>ミナセ住建株式会社</p>
      <p>長野県伊那市春日町 2-14-8<br>TEL 0265-40-7712</p>
    </div>
  </div>
  <p class="copyright">Copyright (C) Morvatu All Rights Reserved.</p>
</footer>

</body>
</html>
```